Postcard flyer for body postive dance classes

We need an eye catching double sided A6 postcard for body positive dance classes. The business name is stepbloomjoy and already have a rough logo and some text that needs tidying up and putting together. The design needs to be simple and elegant. We are appealing to a diverse range of adult women with or without dance experience to join us in a safe, supportive and creative environment. We would like the design to use black, white and a soft green. The final design should communicate movement, contentment and wholeness. File with information attached.

Target Market(s)

Diverse range of adult women

Industry/Entity Type

Health And Wellness

Font styles to use
Other font styles liked:
• Candara or similar but open to suggestions

Colors
abd036
cadf82
eaf2ce
fffefb
fef9ed
fff3d1
ffffff

Requirements
Must have
• Logo and text provided.
Nice to have
• Sense of movement. Match to website colours and style.
Should not have
• Intimidating perfect body images

```html
<!DOCTYPE html>
<html lang="en">
<head>
<meta charset="utf-8">
<title>stepbloomjoy – postcard</title>
<link rel="stylesheet" href="https://fonts.googleapis.com/css2?family=Arimo:wght@400;700&family=Yellowtail&display=swap">
<style>
  :root {
    --page-bg: #eef6fa;
    --mint: #a9e0d6;
    --mint-band: #dff3ef;
    --charcoal: #4a4f4e;
    --ink: #222222;
    --sky: #3aa3dc;
    --sand: #f6d7a7;
    --sand-light: #fbe9cc;
    --white: #ffffff;
  }
  * { box-sizing: border-box; margin: 0; padding: 0; }
  html, body { width: 919px; height: 1200px; overflow: hidden; }
  body { background: var(--page-bg); position: relative; font-family: "Arimo", Arial, sans-serif; }

  .card { position: absolute; left: 126px; width: 703px; height: 471px; }

  /* Front */
  .card-front { top: 70px; background: var(--mint); }
  .brand {
    position: absolute; left: 0; right: 0; top: 150px;
    display: flex; align-items: center; justify-content: center; gap: 14px;
    font-family: "Arimo", Arial, sans-serif; font-size: 40px; font-weight: 700; color: var(--charcoal);
  }
  .brand-dot { width: 22px; height: 22px; border-radius: 50%; background: var(--charcoal); }
  .tagline {
    position: absolute; left: 0; right: 0; top: 305px; text-align: center;
    font-family: "Yellowtail", cursive; font-size: 36px; color: var(--sky);
  }
  .contact-band {
    position: absolute; left: 0; right: 0; top: 374px; height: 58px;
    background: var(--mint-band); text-align: center;
    font-size: 15px; line-height: 20px; color: var(--ink); padding-top: 10px;
  }

  /* Back */
  .card-back { top: 600px; background: var(--white); padding: 18px 21px; }
  .back-inner { position: relative; width: 100%; height: 100%; background: var(--sand); }
  .back-panel { position: absolute; top: 0; bottom: 0; left: 331px; width: 253px; background: var(--sand-light); }
  .headline { position: absolute; font-family: "Yellowtail", cursive; color: var(--sky); line-height: 1; white-space: nowrap; }
  .headline-big { font-size: 80px; }
  .headline-small { font-size: 50px; }
  .headline-small .is { font-size: 32px; }
  .stars { position: absolute; left: 389px; top: 30px; }
  .pitch {
    position: absolute; left: 344px; top: 72px; width: 227px;
    text-align: center; font-size: 15.5px; line-height: 19px; color: var(--ink);
  }
  .pitch p + p { margin-top: 17px; }
  .ribbon { position: absolute; left: 300px; top: 347px; }
  .ribbon-text {
    position: absolute; left: 300px; top: 353px; width: 315px; text-align: center;
    color: var(--white); font-size: 21px; line-height: 24px;
  }
</style>
</head>
<body>
  <section class="card card-front">
    <div class="brand"><span class="brand-dot"></span>stepbloomjoy</div>
    <p class="tagline">movement, contentment, wholeness</p>
    <div class="contact-band">
      <p>E: maya@stepbloomjoy.com.au - P: 0400517264</p>
      <p>www.stepbloomjoy.com.au - Westvale/Hillcrest</p>
    </div>
  </section>

  <section class="card card-back">
    <div class="back-inner">
      <div class="back-panel"></div>
      <span class="headline headline-big" style="left:20px;top:40px;">Dance</span>
      <span class="headline headline-small" style="left:105px;top:128px;"><span class="is">is</span>joy,</span>
      <span class="headline headline-big" style="left:20px;top:220px;">dance</span>
      <span class="headline headline-small" style="left:105px;top:300px;"><span class="is">is</span> love</span>

      <svg class="stars" width="130" height="30" viewBox="0 0 130 30" aria-hidden="true">
        <g fill="var(--sky)">
          <polygon points="10,12 12,17 17,17 13,20 15,25 10,22 5,25 7,20 3,17 8,17"/>
          <polygon points="36,6 38.5,12 45,12 40,16 42,22 36,18.5 30,22 32,16 27,12 33.5,12"/>
          <polygon points="65,1 68,9 76,9 70,14 72,22 65,17.5 58,22 60,14 54,9 62,9"/>
          <polygon points="94,6 96.5,12 103,12 98,16 100,22 94,18.5 88,22 90,16 85,12 91.5,12"/>
          <polygon points="120,12 122,17 127,17 123,20 125,25 120,22 115,25 117,20 113,17 118,17"/>
        </g>
      </svg>

      <div class="pitch">
        <p>Dance is a the core of our being, a celebration of movement, vitality and wholeness.</p>
        <p>If you’ve never danced beforehand and always wanted to or you want to ignite your past love of dance, join us at stepbloomjoy to start your journey.</p>
      </div>

      <svg class="ribbon" width="320" height="68" viewBox="0 0 320 68" aria-hidden="true">
        <polygon points="0,0 320,0 306,34 320,68 0,68 14,34" fill="var(--sky)"/>
      </svg>
      <p class="ribbon-text">Flow with life through your inner dancer.</p>
    </div>
  </section>
</body>
</html>
```